Harbor Rest Company Needs Business Card

Looking for a very nice looking business card. Creative but not extravagant. We sell beds and pillows across the U.S. and need something professional but catchy. I have attached the logo.

Name : Dale Morton
Title : President
Phone : (800) 417-2960
Email: rest@quiltano.com
Website: www.quiltano.com

Can be single-sided or double-sided
horizontal or vertical

Can use Blues/Greys

Target Market(s)

Mass Market

Industry/Entity Type

Retail

Contact Information for Business Card

Name : Dale Morton
Title : President
Phone : (800) 417-2960
Email: rest@quiltano.com
Website: www.quiltano.com

Requirements
Must have
• Clean, Modern, Smooth
• Can use Blues/Greys
• On the other side without the information - have something simple like www.quiltano.com or our logo
Nice to have
• Surprise me
Should not have
• Nothing crazy, nothing cluttered

```html
<!DOCTYPE html>
<html lang="en">
<head>
<meta charset="utf-8">
<title>Harbor Rest Company – Business Card</title>
<link href="https://fonts.googleapis.com/css2?family=PT+Sans:wght@400;700&display=swap" rel="stylesheet">
<style>
  :root {
    --page: #ffffff;
    --card-dark: #1b1b1b;
    --card-light: #f4f9fc;
    --brand-blue: #2fa6d9;
    --ink: #111111;
    --ink-soft: #222222;
    --icon: #ffffff;
  }
  html, body {
    margin: 0;
    padding: 0;
    overflow: hidden;
    background: var(--page);
  }
  .canvas {
    position: relative;
    width: 1200px;
    height: 1000px;
    background: var(--page);
    font-family: "PT Sans", sans-serif;
    overflow: hidden;
  }
  .card {
    position: absolute;
  }
  .card--front {
    left: 227px;
    top: 37px;
    width: 746px;
    height: 426px;
    background: var(--card-dark);
    display: flex;
    align-items: center;
    justify-content: center;
  }
  .brand-name {
    margin: 0;
    color: var(--brand-blue);
    font-family: "PT Sans", sans-serif;
    font-weight: 400;
    line-height: 1;
    letter-spacing: 0.02em;
  }
  .card--front .brand-name {
    font-size: 150px;
    margin-top: -12px;
  }
  .card--back {
    left: 231px;
    top: 488px;
    width: 749px;
    height: 428px;
    background: var(--card-light);
  }
  .identity {
    position: absolute;
    left: 40px;
    top: 100px;
    width: 278px;
    text-align: center;
  }
  .card--back .brand-name {
    font-size: 84px;
  }
  .person-name {
    margin: 26px 0 0;
    font-weight: 700;
    font-size: 36px;
    line-height: 1;
    color: var(--ink);
    letter-spacing: -0.01em;
  }
  .person-title {
    margin: 2px 0 0;
    font-weight: 400;
    font-size: 44px;
    line-height: 1;
    color: var(--ink-soft);
  }
  .contact-rail {
    position: absolute;
    left: 371px;
    top: 64px;
    width: 66px;
    height: 364px;
  }
  .contact-list {
    list-style: none;
    margin: 0;
    padding: 0;
    position: absolute;
    left: 482px;
    top: 0;
  }
  .contact-item {
    position: absolute;
    left: 0;
    white-space: nowrap;
    font-size: 21px;
    line-height: 1;
    color: var(--ink);
    transform: translateY(-50%);
  }
  .contact-item--phone { top: 97px; }
  .contact-item--email { top: 222px; }
  .contact-item--web { top: 342px; }
</style>
</head>
<body>
<div class="canvas">

  <section class="card card--front" aria-label="Card front">
    <p class="brand-name">quiltano</p>
  </section>

  <section class="card card--back" aria-label="Card back">
    <div class="identity">
      <p class="brand-name">quiltano</p>
      <p class="person-name">DALE MORTON</p>
      <p class="person-title">President</p>
    </div>

    <svg class="contact-rail" viewBox="0 0 66 364" aria-hidden="true">
      <line x1="33" y1="33" x2="33" y2="364" stroke="var(--brand-blue)" stroke-width="2"/>

      <g class="icon icon--phone" transform="translate(33 33)">
        <circle r="32" fill="var(--brand-blue)"/>
        <path d="M-14 -18 l7 -3 l6 11 l-5 4 c3 7 7 11 14 14 l4 -5 l11 6 l-3 7 c-2 3 -6 4 -10 2 c-11 -5 -19 -13 -24 -24 c-2 -4 -2 -9 0 -12 z"
              fill="var(--icon)"/>
      </g>

      <g class="icon icon--email" transform="translate(33 158)">
        <circle r="32" fill="var(--brand-blue)"/>
        <rect x="-21" y="-14" width="42" height="28" fill="none" stroke="var(--icon)" stroke-width="2.5"/>
        <polyline points="-21,-14 0,4 21,-14" fill="none" stroke="var(--icon)" stroke-width="2.5"/>
        <line x1="-21" y1="14" x2="-6" y2="-1" stroke="var(--icon)" stroke-width="2.5"/>
        <line x1="21" y1="14" x2="6" y2="-1" stroke="var(--icon)" stroke-width="2.5"/>
      </g>

      <g class="icon icon--link" transform="translate(33 278) rotate(-35)">
        <circle r="32" transform="rotate(35)" fill="var(--brand-blue)"/>
        <rect x="-22" y="-7" width="24" height="14" rx="7" fill="none" stroke="var(--icon)" stroke-width="3.5"/>
        <rect x="-2" y="-7" width="24" height="14" rx="7" fill="none" stroke="var(--icon)" stroke-width="3.5"/>
      </g>
    </svg>

    <ul class="contact-list">
      <li class="contact-item contact-item--phone">(800) 417-2960</li>
      <li class="contact-item contact-item--email">rest@quiltano.com</li>
      <li class="contact-item contact-item--web">www.quiltano.com</li>
    </ul>
  </section>

</div>
</body>
</html>
```